Business Card Design

We are a radiology group

We are working to move into new service centers

We want to communicate innovation and bringing our customers ahead with technology and outstanding results
Updates

I have uploaded a high resolution logo as requested :-)

Target Market(s)

hospitals, clinics

Industry/Entity Type

Business

Contact Information for Business Card

Deborah L. Pettigrew, MBA, CIIP
CTIO
deborah.pettigrew@tdrpc-mail.com
cell 518-476-2913
www.tdrpc-mail.com
Tidewater Diagnostic Radiology, PC

```html
<!DOCTYPE html>
<html lang="en">
<head>
<meta charset="utf-8">
<title>Tidewater Diagnostic Radiology – Business Card</title>
<link rel="stylesheet" href="https://fonts.googleapis.com/css2?family=Lato:wght@400;700;900&display=swap">
<style>
  :root {
    --page-bg: #e9ecef;
    --card-bg: #ffffff;
    --brand-blue: #1b87c5;
    --brand-blue-light: #3aa3dc;
    --sky: #8cc8ea;
    --dot: #a9d6f0;
    --muted: #5a6770;
  }
  * { margin: 0; padding: 0; box-sizing: border-box; }
  html, body {
    width: 1200px; height: 447px; overflow: hidden;
    background: var(--page-bg);
    font-family: "Lato", sans-serif;
  }
  .stage {
    width: 1200px; height: 447px;
    display: flex; align-items: center; justify-content: center;
  }
  .business-card {
    position: relative;
    width: 700px; height: 400px;
    background: var(--card-bg);
    box-shadow: 0 6px 20px rgba(0,0,0,.18);
    overflow: hidden;
  }
  .header-band {
    position: absolute; left: 0; top: 0; width: 100%; height: 58px;
    background: linear-gradient(180deg, var(--brand-blue-light), var(--brand-blue));
    display: flex; align-items: center; justify-content: center;
  }
  .header-band h1 {
    color: #fff; font-weight: 900; font-size: 25px;
    letter-spacing: .5px; text-transform: uppercase;
  }
  .contact {
    position: absolute; left: 42px; top: 122px;
  }
  .contact .name {
    color: var(--brand-blue); font-weight: 900; font-size: 19px;
    text-transform: uppercase; letter-spacing: .3px;
  }
  .contact .role {
    color: var(--sky); font-size: 16px; margin-top: 1px;
  }
  .contact .phone {
    display: flex; align-items: center; gap: 10px;
    color: var(--brand-blue); font-size: 18px; margin-top: 22px;
  }
  .services {
    position: absolute; right: 22px; top: 70px; text-align: right;
  }
  .services h2 {
    color: var(--sky); font-weight: 400; font-size: 18px;
    margin-right: 16px; margin-bottom: 2px;
  }
  .services ul { list-style: none; }
  .services li {
    color: var(--muted); font-size: 13.5px; line-height: 17.5px;
  }
  .services li::after {
    content: ""; display: inline-block;
    width: 8px; height: 8px; border-radius: 50%;
    background: var(--dot); margin-left: 7px; vertical-align: 0;
  }
  .web-pill {
    position: absolute; right: 0; bottom: 22px;
    height: 34px; padding: 0 24px 0 34px;
    background: var(--brand-blue); color: #fff;
    border-radius: 17px 0 0 17px;
    display: flex; align-items: center;
    font-size: 17px; font-weight: 700;
  }
  .company-name {
    position: absolute; left: 42px; bottom: 29px;
    color: var(--brand-blue); font-weight: 400; font-size: 18px;
  }
</style>
</head>
<body>
<main class="stage">
  <article class="business-card">
    <header class="header-band"><h1>Tidewater Diagnostic Radiology</h1></header>

    <section class="contact">
      <p class="name">Deborah L. Pettigrew</p>
      <p class="role">Director</p>
      <p class="phone">
        <svg width="12" height="18" viewBox="0 0 12 18" aria-hidden="true">
          <rect x="1" y="1" width="10" height="16" rx="2" fill="none" stroke="#1b87c5" stroke-width="1.6"/>
          <line x1="4.5" y1="14" x2="7.5" y2="14" stroke="#1b87c5" stroke-width="1.4"/>
        </svg>
        518-476-2913
      </p>
    </section>

    <section class="services">
      <h2>Our Services</h2>
      <ul>
        <li>General Radiology</li>
        <li>Digital Mammography and Stereotactic Biopsies</li>
        <li>Neuro and Musculoskeletal Imaging (CT, MRI)</li>
        <li>PET Scanning</li>
        <li>Nuclear Medicine</li>
        <li>Osteoporosis Screening (DEXA and QCT)</li>
        <li>Vascular Imaging (Ultrasound and Angiography)</li>
        <li>Ultrasound</li>
        <li>Pain Management</li>
        <li>Interventional Radiology</li>
        <li>Cardiac Imaging</li>
      </ul>
    </section>

    <p class="company-name">Tidewater Diagnostic Radiology</p>
    <p class="web-pill">www.tdrpc-mail.com</p>
  </article>
</main>
</body>
</html>
```